hi all

Im after a new age looking business card with my company logo on it

must include these details, I would like the PH and Email to be symbols

If the colours used for card could be kept within the colours used in logo that I have supplied that would be great, if another colour is to be used dark grey would be ok. no light bulbs etc thanks

Details below to be incorporated on card

Damian Holloway

Lic E871302

PH 0219647381

E info@brightvaleelectrical.example.nz

Domestic Commercial Industrial Electricians

```html
<!DOCTYPE html>
<html lang="en">
<head>
<meta charset="utf-8">
<title>Brightvale Electrical – Business Card</title>
<link href="https://fonts.googleapis.com/css2?family=Raleway:wght@700;800&family=Arimo&family=Open+Sans:wght@400&display=swap" rel="stylesheet">
<style>
  :root {
    --backdrop: #d9d9d9;
    --card-black: #000000;
    --brand-blue: #1274be;
    --text-white: #ffffff;
  }
  * { box-sizing: border-box; margin: 0; padding: 0; }
  html, body { width: 1200px; height: 802px; overflow: hidden; }
  body { background: var(--backdrop); position: relative; }

  .card {
    position: absolute;
    top: 274px;
    width: 443px;
    height: 265px;
    background: var(--card-black);
    overflow: hidden;
    box-shadow: 0 3px 8px rgba(0,0,0,0.35);
  }
  .card--front { left: 136px; }
  .card--back { left: 624px; }

  .accent-panel { position: absolute; inset: 0; width: 100%; height: 100%; }

  .wordmark {
    position: absolute;
    color: var(--brand-blue);
    font-family: "Raleway", sans-serif;
    font-weight: 800;
    line-height: 1;
  }
  .wordmark__main { display: block; font-size: 30px; letter-spacing: 1px; }
  .wordmark__sub { display: block; font-size: 12px; letter-spacing: 3.4px; text-align: right; margin-top: 3px; }

  .card--front .wordmark { left: 24px; top: 50px; }

  .holder-name {
    position: absolute; left: 24px; top: 148px;
    font-family: "Raleway", sans-serif; font-weight: 700;
    font-size: 16px; color: var(--brand-blue);
  }
  .licence {
    position: absolute; left: 25px; top: 178px;
    font-family: "Arimo", sans-serif; font-size: 13px; color: var(--text-white);
  }
  .contact-list { position: absolute; left: 25px; top: 210px; list-style: none; }
  .contact-item {
    display: flex; align-items: center; gap: 3px;
    font-family: "Arimo", sans-serif; font-size: 12.5px; color: var(--text-white);
    line-height: 16px;
  }
  .contact-icon { width: 13px; height: 13px; flex: none; }

  .card--back .wordmark { left: 0; right: 0; top: 120px; text-align: center; }
  .card--back .wordmark__main { font-size: 34px; }
  .card--back .wordmark__sub { text-align: center; font-size: 13px; letter-spacing: 4px; }

  .service-band {
    position: absolute; left: 0; top: 203px; width: 100%; height: 30px;
    background: var(--brand-blue);
    display: flex; align-items: center; justify-content: center;
    font-family: "Open Sans", sans-serif; font-size: 10.5px; color: var(--text-white);
    letter-spacing: 0.2px;
  }
</style>
</head>
<body>

<section class="card card--front">
  <svg class="accent-panel" viewBox="0 0 443 265" aria-hidden="true">
    <polygon points="334,0 443,0 443,265 307,265" fill="var(--brand-blue)"/>
  </svg>

  <div class="wordmark">
    <span class="wordmark__main">BRIGHTVALE</span>
    <span class="wordmark__sub">ELECTRICAL</span>
  </div>

  <p class="holder-name">DAMIAN HOLLOWAY</p>
  <p class="licence">Lic E871302</p>

  <ul class="contact-list">
    <li class="contact-item">
      <svg class="contact-icon" viewBox="0 0 14 14" aria-label="Phone">
        <rect x="0.7" y="0.7" width="12.6" height="12.6" rx="2" fill="none" stroke="var(--brand-blue)" stroke-width="1.3"/>
        <path d="M4.2 3.2 l1.5 0 l0.6 2 l-1 0.8 q0.8 1.8 2.6 2.6 l0.8 -1 l2 0.6 l0 1.5 q-4.5 0.5 -6.5 -6.5z" fill="var(--brand-blue)"/>
      </svg>
      <span>0219647381</span>
    </li>
    <li class="contact-item">
      <svg class="contact-icon" viewBox="0 0 14 14" aria-label="Email">
        <rect x="0.5" y="2.5" width="13" height="9" fill="var(--brand-blue)"/>
        <path d="M0.5 2.5 L7 8 L13.5 2.5" fill="none" stroke="var(--card-black)" stroke-width="1"/>
      </svg>
      <span>info@brightvaleelectrical.example.nz</span>
    </li>
  </ul>
</section>

<section class="card card--back">
  <div class="wordmark">
    <span class="wordmark__main">BRIGHTVALE</span>
    <span class="wordmark__sub">ELECTRICAL</span>
  </div>
  <p class="service-band">DOMESTIC COMMERCIAL INDUSTRIAL ELECTRICIANS</p>
</section>

</body>
</html>
```